Speisekarten für griechisches Restaurant
Zielgruppe
modernes griechisches Restaurant
Aufgabenstellung
neues modernen helles design ,
nach Durchsicht aus meinen Vorlangen, sollten ein paar Anpassung am text und preisen noch durchgeführt werden.
aus der pdf datei,, ist ab Seite 7 die richtige Speisekarte,, vorher sind nur entwürfe vom mir, diese bitte ignorieren.

```html
<!DOCTYPE html>
<html lang="de">
<head>
<meta charset="utf-8">
<title>Lefkada – Speisekarte</title>
<link rel="stylesheet" href="https://fonts.googleapis.com/css2?family=Dancing+Script:wght@500&family=Open+Sans:wght@400&display=swap">
<style>
  :root {
    --backdrop: #d9dad3;
    --paper: #ffffff;
    --frame-line: #dfe4cc;
    --ink: #4a4a4a;
    --ink-soft: #6b6b6b;
    --branch-tint: #eef0e4;
  }
  html, body {
    margin: 0;
    padding: 0;
    width: 1200px;
    height: 900px;
    overflow: hidden;
    background: var(--backdrop);
  }
  .menu-cover {
    position: absolute;
    left: 303px;
    top: 30px;
    width: 594px;
    height: 840px;
    background: var(--paper);
    box-shadow: 0 4px 18px rgba(0,0,0,0.12);
  }
  .cover-frame {
    position: absolute;
    left: 52px;
    top: 60px;
    right: 52px;
    bottom: 60px;
    border: 1px solid var(--frame-line);
  }
  .branch-art {
    position: absolute;
    left: 40px;
    top: 270px;
    width: 360px;
    height: 500px;
    background: radial-gradient(ellipse at 50% 50%, var(--branch-tint) 0%, rgba(238,240,228,0.4) 55%, rgba(255,255,255,0) 75%);
  }
  .restaurant-name {
    position: absolute;
    right: 80px;
    top: 112px;
    margin: 0;
    font-family: "Open Sans", sans-serif;
    font-weight: 400;
    font-size: 24px;
    line-height: 1;
    letter-spacing: 6px;
    text-transform: uppercase;
    color: var(--ink-soft);
  }
  .cover-title {
    position: absolute;
    left: 0;
    right: 0;
    top: 215px;
    margin: 0;
    text-align: center;
    font-family: "Dancing Script", cursive;
    font-weight: 500;
    font-size: 104px;
    line-height: 1;
    color: var(--ink);
    letter-spacing: 1px;
  }
</style>
</head>
<body>
  <main class="menu-cover">
    <div class="cover-frame"></div>
    <div class="branch-art" role="img" aria-label="Zarte Linienzeichnung eines Olivenzweigs mit Blättern und Oliven"></div>
    <p class="restaurant-name">Lefkada</p>
    <h1 class="cover-title">Speisekarte</h1>
  </main>
</body>
</html>
```